Tri-Fold Menu of Services for our Eyelash and Skin Care Spa

We need a beautiful spa service menu for our upscale spa in St. Charles Missouri. We specialize in providing treatments that are specific to the clients needs. Our services are eyelash extensions, skin care treatments, full body waxing and makeup application. Our spa colors are dark purples and greys and we are not opposed to additional colors that would complement those colors. We do a lot of eyelash extensions and while we do what those services listed we would like the skin care treatments to be in an area that would be noticed first. One of the attachments lists all of our services, descriptions and prices (please be sure to include all services and pricing. descriptions if possible). And our website has more information about us if needed. The website was not professionally done. So it DOESN'T represent our style exactly.

I HAVE ATTACHED A FEW PHOTOS BUT THEY DON'T HAVE TO BE USED.

Target Market(s)

women who would like to look their best, 35-55, annual income of 100,000+, she is usually busy and her children (if she has any) are high school age or older.

Industry/Entity Type

It Service

Font styles to use
Serif
Sans Serif

Requirements
Must have
• Must list all of our services. If it works to have the descriptions that would be great.
Nice to have
• If it works to have the descriptions of each service that would be great.

```html
<!DOCTYPE html>
<html lang="en">
<head>
<meta charset="utf-8">
<title>Lumaire Lash &amp; Skin Spa – Services</title>
<link rel="stylesheet" href="https://fonts.googleapis.com/css2?family=Montserrat:wght@400;600;700&display=swap">
<style>
  :root{
    --violet-deep:#452b80;
    --violet-head:#4b1c8e;
    --lavender:#e5dcec;
    --ink:#1c1430;
    --body:#4a4552;
    --rule:#8c8494;
    --mint:#80ffc4;
    --white:#ffffff;
  }
  *{margin:0;padding:0;box-sizing:border-box}
  html,body{width:1200px;height:855px;overflow:hidden}
  body{background:var(--lavender);font-family:'Montserrat',Arial,sans-serif;color:var(--body);position:relative}
  .menu{position:relative;width:1200px;height:855px;overflow:hidden}
  .topbar{position:absolute;left:0;top:0;width:1200px;height:55px;background:var(--violet-deep)}
  .topbar-title{position:absolute;left:62px;top:22px;color:var(--white);font-weight:700;font-size:20px;letter-spacing:3px;line-height:1}
  .brand{position:absolute;left:826px;top:18px;color:var(--white);font-weight:600;font-size:15px;letter-spacing:.5px;line-height:1;display:flex;align-items:center;gap:7px}
  .brand-dot{width:9px;height:9px;border-radius:50%;background:var(--white)}
  .col-divider{position:absolute;top:72px;bottom:0;border-left:1px dashed #c7bcd2}
  .rule{position:absolute;height:0;border-top:1.5px solid var(--rule)}
  .icon{position:absolute;width:38px;height:38px;border-radius:50%;background:var(--violet-deep)}
  .section-title{position:absolute;color:var(--violet-head);font-weight:700;font-size:15.5px;letter-spacing:2.2px;line-height:1.1;white-space:nowrap}
  .section-title.tight{letter-spacing:1.5px}
  .service{position:absolute}
  .service h3{color:var(--violet-head);font-weight:700;font-size:11.6px;letter-spacing:.3px;line-height:14px}
  .service .cost{color:var(--ink);font-weight:700;font-size:12.2px;line-height:14px;margin-top:5px}
  .service p{font-size:10.1px;line-height:12.6px;letter-spacing:0}
  .service p + p{margin-top:12.6px}
  .list-title{position:absolute;color:var(--ink);font-weight:700;font-size:12px;letter-spacing:.3px;line-height:14px}
  .list-title.violet{color:var(--violet-head)}
  .price-list{position:absolute;display:grid;font-size:10.1px;line-height:12.6px;letter-spacing:.1px}
  .addons{grid-template-columns:201px 50px}
  .four{grid-template-columns:101px 50px 101px auto}
  .tint{grid-template-columns:101px 50px 74px auto}
  .massage{grid-template-columns:201px 51px auto}
  .note{position:absolute;font-size:10.1px;line-height:12.6px;letter-spacing:.1px;width:290px}
  .wave{position:absolute;left:0;top:0}
</style>
</head>
<body>
<main class="menu">
  <header class="topbar">
    <div class="topbar-title">SERVICES</div>
    <div class="brand"><span class="brand-dot"></span>Lumaire Lash &amp; Skin Spa</div>
  </header>

  <svg class="wave" width="1200" height="855" viewBox="0 0 1200 855" aria-hidden="true">
    <path d="M0,811 C300,817 520,800 650,803 C720,806 770,835 795,855 L765,855 C700,836 600,828 450,830 C300,833 150,838 0,836 Z" fill="var(--mint)"/>
  </svg>

  <div class="col-divider" style="left:405px"></div>
  <div class="col-divider" style="left:796px"></div>

  <div class="icon" style="left:39px;top:71px" role="img" aria-label="Icon of a woman's profile"></div>
  <div class="section-title" style="left:92px;top:75px">FACIAL &amp; SKIN<br>TREATMENTS</div>
  <div class="rule" style="left:39px;width:366px;top:127px"></div>

  <section class="service" style="left:40px;top:158px;width:355px">
    <h3>ESSENTIAL DEEP CLEANSING TREATMENT</h3>
    <div class="cost">Cost: $65 . Duration: 60 min</div>
    <p>This relaxing, purifying treatment consists of steaming, ex-foliation, and an intense deeper cleansing of clogged pores. A skin-type specific ampoule is gently massaged into the skin of your face, neck, and decollete, followed by a therapist selected mask. Beneficial for all skin types.</p>
  </section>

  <section class="service" style="left:40px;top:284px;width:355px">
    <h3>MINI FACIAL</h3>
    <div class="cost">Cost: $48 . Duration: 30 min</div>
    <p>This express facial is ideal for those on the go. Your skin is cleansed, lightly ex-foliated and gently massaged. A porerefining mask is then applied, followed by a veil of light moisturizer.</p>
  </section>

  <section class="service" style="left:40px;top:386px;width:355px">
    <h3>AROMATHERAPY FACIAL</h3>
    <div class="cost">Cost: $75 . Duration: 60 min</div>
    <p>Our Aromatherapy facial will naturally enhance the facial benefits using fragrant oils extracted from flowers, fruits and herbs.</p>
  </section>

  <section class="service" style="left:40px;top:475px;width:345px">
    <h3>LUMINELLE LIFT &amp; GLOW TREATMENT FACIAL</h3>
    <div class="cost">Cost: $95 . Duration: 60 min</div>
    <p>Seeking a treatment with amazing instant results? Redefining radiance and facial contouring, this exclusively formulated treatment features the latest in freezedried technology to deliver instant results and cumulative skin care benefits. Ideal for any skin type showing signs of aging, or as the perfect instant repair boost when you want to look your best. Proven to perform, the Velora Luminelle Lift &amp; Glow facial renders your skin ultra-luminous with a firmer, tighter, and more youthfully defined appearance.</p>
  </section>

  <section class="service" style="left:40px;top:654px;width:345px">
    <h3>SOOTHING BOTANOVA TREATMENT FACIAL</h3>
    <div class="cost">Cost: $100 . Duration: 60 min</div>
    <p>This highly effective, soothing treatment calms redness and alleviates irritated or sensitive skin. A healing Propolis ampoule (natural ingredient collected by bees) is applied to desensitize the skin’s surface and strengthen capillaries. A cooling liftoff mask is then applied to seal in the vitamin enriched beneficial ampoule.</p>
  </section>

  <section class="service" style="left:428px;top:76px;width:365px">
    <h3>RADIANCE PHOTOTHERAPY TREATMENT</h3>
    <div class="cost">Cost: $150 . Package x 8: $800</div>
    <p>Uses heat and light energy to gently break up areas of excess pigment while stimulating the production of new collagen. Improved skin tone, less spots, fewer pink areas, less redness, reduction in fine lines and wrinkles. Diminishes pores and restores natural radiant glow of skin. Like laser treatments MicroPhotoTherapy treats skin with therapeutic light energy but unlike laser treatments, Micro Photo Therapy features gentle waves of heat and light that improve the skin with no downtime and very little discomfort.</p>
    <p>We recommend 8 treatments 1 to 2 times a week for best results.</p>
  </section>

  <section class="service" style="left:428px;top:254px;width:365px">
    <h3>DIAMOND MICRODERMABRASION TREATMENT</h3>
    <div class="cost">Cost: $78</div>
    <p>With this treatment you will see softening of fine lines and wrinkles and smoothing of coarsely textured skin. Dull, stressed or congested skin will be brighter and clearer. The appearance of enlarged pores, and acne scars will be minimized. Your at home products will be able to penetrate deeper therefore, are more effective.</p>
    <p>Or add this to any facial or most peels for just $30.</p>
  </section>

  <div class="rule" style="left:428px;width:761px;top:396px"></div>
  <div class="icon" style="left:428px;top:403px" role="img" aria-label="Sun icon for peels"></div>
  <div class="section-title" style="left:480px;top:415px">PEELS</div>
  <div class="rule" style="left:428px;width:761px;top:448px"></div>

  <section class="service" style="left:437px;top:475px;width:340px">
    <h3>ACNE LIFT PEEL</h3>
    <div class="cost">Cost: $50 X 1 . $250 X 6 . Duration: 30 min</div>
    <p>Mild to moderate Acne peel</p>
  </section>
  <section class="service" style="left:437px;top:537px;width:340px">
    <h3>LIGHTENING LIFT PEEL</h3>
    <div class="cost">Cost: $50 X 1 . $250 X 6 . Duration: 30 min</div>
    <p>Pigmentation (sun/brown spots), uneven skin tone</p>
  </section>
  <section class="service" style="left:437px;top:598px;width:340px">
    <h3>WRINKLE LIFT</h3>
    <div class="cost">Cost: $50 X 1 . $250 X 6 . Duration: 30 min</div>
    <p>Aging, fine lines and wrinkles</p>
  </section>
  <section class="service" style="left:437px;top:661px;width:340px">
    <h3>SIGNATURE LIFT</h3>
    <div class="cost">Cost: $50 X 1 . $250 X 6 . Duration: 30 min</div>
    <p>&nbsp;Rosacea, dry/dehydrated</p>
  </section>
  <section class="service" style="left:437px;top:722px;width:265px">
    <h3>PERFECTION LIFT</h3>
    <div class="cost" style="white-space:nowrap">Cost: $100X 1 . $350 X 6 . Duration: 30 min</div>
    <p>Advanced Aging, Acne, and Pigmentation (slightly more aggressive than the other options)</p>
  </section>

  <div class="list-title" style="left:824px;top:73px">PEEL ADD ONS</div>
  <div class="price-list addons" style="left:824px;top:99px">
    <span>Microdermabrasion</span><span>$30</span>
    <span>Luminelle Lift &amp; Glow Eye Treatment</span><span>$20</span>
    <span>Hot or Cold Stones</span><span>$15</span>
    <span>Extended Massage</span><span>$15</span>
    <span>Peppermint Scalp Massage</span><span>$15</span>
    <span>Foot Scrub &amp; Massage</span><span>$20</span>
    <span>Aromatherapy</span><span>$10</span>
    <span>Specialty Ampoule</span><span>$15</span>
    <span>Specialty Mask</span><span>$13</span>
  </div>
  <div class="rule" style="left:824px;width:291px;top:227px"></div>
  <div class="icon" style="left:825px;top:232px" role="img" aria-label="Mascara wand icon"></div>
  <div class="section-title" style="left:876px;top:244px">EYELASHES</div>
  <div class="rule" style="left:824px;width:291px;top:276px"></div>

  <div class="list-title violet" style="left:824px;top:291px">CLASSIC</div>
  <div class="price-list four" style="left:824px;top:305px">
    <span>Full Set</span><span>$175</span><span>Demi Set</span><span>$110</span>
    <span>Touch up</span><span>$60</span><span></span><span></span>
  </div>
  <div class="list-title" style="left:824px;top:344px">VOLUME TECHNIQUE</div>
  <div class="price-list four" style="left:824px;top:358px">
    <span>Full Set</span><span>$220</span><span>Demi Set</span><span>$135</span>
    <span>Touch up</span><span>$72</span><span></span><span></span>
  </div>

  <div class="icon" style="left:823px;top:403px" role="img" aria-label="Closed eye icon"></div>
  <div class="section-title tight" style="left:876px;top:415px">WAXING &amp; TINTING</div>
  <div class="icon" style="left:1078px;top:403px" role="img" aria-label="Figure icon for body waxing"></div>

  <div class="list-title violet" style="left:824px;top:465px">WAXING</div>
  <div class="price-list four" style="left:824px;top:479px">
    <span>Eyebrows</span><span>$17</span><span>Upper Lip</span><span>$14</span>
    <span>Chin</span><span>$14</span><span>Sides of face</span><span>$14</span>
    <span>Bikini</span><span>$27+</span><span>Brazilian</span><span>$55+</span>
    <span>Underarm</span><span>$22</span><span>Arms Full</span><span>$35</span>
    <span>Lower</span><span>$26</span><span>Legs Full</span><span>$62</span>
    <span>Lower</span><span>$40</span><span>Chest</span><span>$44</span>
    <span>Back</span><span>$44</span><span></span><span></span>
  </div>

  <div class="list-title violet" style="left:824px;top:592px">TINTING</div>
  <div class="price-list tint" style="left:824px;top:606px">
    <span>Eyebrows</span><span>$20</span><span>Eyelashes</span><span>$20</span>
    <span>Both</span><span>$30</span><span></span><span></span>
  </div>

  <div class="rule" style="left:824px;width:291px;top:644px"></div>
  <div class="icon" style="left:824px;top:652px" role="img" aria-label="Butterfly icon for massages"></div>
  <div class="section-title" style="left:876px;top:664px">MASSAGES</div>
  <div class="rule" style="left:824px;width:291px;top:697px"></div>

  <div class="price-list massage" style="left:824px;top:713px">
    <span>Neck, Back &amp; Head Massage</span><span>$45</span><span>30 min</span>
    <span>Aromatherapy Scalp Massage</span><span>$15</span><span>10 min</span>
    <span>Foot Massage and Scrub</span><span>$20</span><span>15 min</span>
    <span>&nbsp;</span><span></span><span></span>
    <span>Headache &amp; Migraine<br>Relief Treatment</span><span>$45</span><span>30 min</span>
  </div>
  <p class="note" style="left:824px;top:788px">Relief from headaches caused by stress, tension, hormonal imbalances or sensitivities using cold stones and massaging techniques for the face.</p>
</main>
</body>
</html>
```